Medical practice in the United States needs a landing page

Our medical practice, based in Dallas, Texas, is called 'Calloway Headache Clinics.' We perform the Calloway Method on patients to treat chronic, severe head pain.

We currently have a landing page for our Chatterbox ads, but we'd like to improve the page's design to increase the lead conversion rate. The landing page contains a form that allows people to register for our free, on-demand informational webinar about the procedure. Either part of the registration form or all of the registration form must be above the fold.

Here is the link to the landing page that needs a more attractive design: https://callowayheadache.example/migraine-treatment-webinars/calloway-treatment-free-patient-webinar/

Once a lead submits the registration form on that page, they are redirected to a different page on the site that contains the webinar video.

Here is a direct link to the page that contains the actual video (note: this is NOT the page for which I am requesting an improved design for this project; I am only including this link so that you can watch the video if you think it will help you create a design for the other page):

https://callowayheadache.example/calloway-headache-clinics-patient-information-webinar/
Updates

Designs look the same

Hello all,

The designs so far have been very impressive! Thank you all for your hard work. Please don't feel compelled to use my exact wording, though, for the description of the webinar. The only requirement is that the form on the page be present and contain the same form fields.

Thanks again!

Target Market(s)

Patients with chronic, severe head pain

Industry/Entity Type

Healthcare

Requirements
Must have
• Either part of the registration form or all of the registration form must be above the fold.
Should not have
• The registration form located completely below the fold.

```html
<!DOCTYPE html>
<html lang="en">
<head>
<meta charset="utf-8">
<title>Webinar Registration – Calloway Headache Clinics</title>
<link href="https://fonts.googleapis.com/css2?family=Fira+Sans:wght@500;600;700&family=Open+Sans:wght@400;600&display=swap" rel="stylesheet">
<style>
:root{
  --teal:#0d4a5e;
  --teal-deep:#0a4c66;
  --green:#8dc63f;
  --green-dark:#17703a;
  --ink:#1c2228;
  --muted:#555d63;
  --field:#f3f3f3;
  --red:#d0101b;
  --night:#1a120c;
}
*{box-sizing:border-box;margin:0;padding:0}
html,body{width:1200px;height:2181px;overflow:hidden;background:#fff}
body{font-family:"Open Sans",sans-serif;color:var(--ink);position:relative}
.page{position:relative;width:1200px;height:2181px;overflow:hidden}
.abs{position:absolute}

/* header */
.topline{left:0;top:0;width:1200px;height:3px;background:var(--teal)}
.header{left:0;top:3px;width:1200px;height:92px;background:#fff}
.brand{left:111px;top:38px;font-family:"Fira Sans",sans-serif;font-weight:500;font-size:20px;color:var(--teal);display:flex;align-items:center;gap:8px}
.brand i{width:10px;height:10px;border-radius:50%;background:var(--green);display:block}
.nav{left:360px;top:44px;display:flex;gap:17px;font-family:"Fira Sans",sans-serif;font-size:11.5px;color:#3c4449}
.nav span.drop::after{content:"⌄";margin-left:4px;font-size:10px}
.consult{left:1057px;top:37px;width:109px;height:32px;background:var(--green);color:#fff;font-family:"Fira Sans",sans-serif;font-weight:600;font-size:11px;letter-spacing:.8px;display:flex;align-items:center;justify-content:center;box-shadow:0 3px 6px rgba(0,0,0,.15)}

/* hero */
.hero{left:0;top:95px;width:1200px;height:543px;background:linear-gradient(180deg,#3d4a66 0%,#6b6c74 35%,#9a7c5a 65%,#5d6b3c 100%)}
.hero-title{left:0;top:268px;width:1200px;text-align:center;font-family:"Fira Sans",sans-serif;font-weight:700;font-size:49px;color:#fff;text-shadow:0 3px 8px rgba(0,0,0,.35)}
.hero-curve{left:0;top:430px}

/* left column */
.intro{left:111px;top:668px;width:400px;font-family:"Fira Sans",sans-serif;font-weight:600;font-size:27px;line-height:39px;color:var(--teal)}
.topics-title{left:111px;top:768px;font-family:"Fira Sans",sans-serif;font-weight:600;font-size:21px;color:#111}
.topic{left:111px;width:372px}
.topic .ico{position:absolute;left:0;top:-7px;width:36px;height:36px;border-radius:50%;background:linear-gradient(180deg,#3f9a3c,#0d4a5e);display:flex;align-items:center;justify-content:center}
.topic h3{position:absolute;left:54px;top:0;font-family:"Fira Sans",sans-serif;font-weight:600;font-size:16px;color:#111}
.topic .caret{position:absolute;right:0;top:2px;font-size:10px;color:#111}
.topic p{position:absolute;left:54px;top:24px;width:318px;font-size:13.5px;line-height:23px;color:var(--muted)}

/* form card */
.card{left:528px;top:426px;width:582px;height:851px;background:#fff;box-shadow:0 4px 22px rgba(0,0,0,.08);border-radius:3px}
.card h2{position:absolute;left:0;top:35px;width:100%;text-align:center;font-family:"Fira Sans",sans-serif;font-weight:600;font-size:28px;color:var(--teal)}
.lbl{position:absolute;font-family:"Fira Sans",sans-serif;font-weight:500;font-size:14px;color:#3c3f42}
.fld{position:absolute;width:250px;height:47px;background:var(--field);font-size:12.5px;color:#555;padding:0 26px;display:flex;align-items:center;justify-content:space-between}
.fld .tri{font-size:9px;color:#444}
.hint{position:absolute;font-size:8.5px;line-height:16px;color:#555;width:250px}
.hint b{color:var(--red);font-weight:400}
.msg{position:absolute;left:29px;top:509px;width:524px;height:106px;background:var(--field);font-size:12.5px;color:#555;padding:16px 26px}
.agree{position:absolute;left:29px;top:675px;display:flex;align-items:center;gap:8px;font-size:9px;color:#555}
.agree i{width:8px;height:8px;border:1px solid #aaa;display:block}
.policy{position:absolute;left:29px;top:707px;width:530px;font-size:12.5px;line-height:21px;color:#555}
.policy a{color:var(--red);text-decoration:underline;font-weight:600}
.submit{position:absolute;left:198px;top:766px;width:184px;height:42px;background:linear-gradient(180deg,#18773a,#0d4a5e);color:#fff;font-family:"Fira Sans",sans-serif;font-weight:600;font-size:15px;display:flex;align-items:center;justify-content:center}

/* testimonial */
.footer-bg{left:0;top:1700px;width:1200px;height:481px;background:var(--teal-deep)}
.testimonial{left:0;top:1397px}
.quote-mark{left:0;top:1490px;width:1200px;text-align:center;font-family:"Fira Sans",sans-serif;font-weight:700;font-size:62px;color:#fff;line-height:1}
.quote{left:200px;top:1556px;width:800px;text-align:center;font-size:17px;line-height:34px;color:#fff}
.author{left:0;top:1639px;width:1200px;text-align:center;font-family:"Fira Sans",sans-serif;font-weight:600;font-size:17px;color:var(--green)}
.dots{left:589px;top:1767px;display:flex;gap:4px}
.dots i{width:4px;height:4px;border-radius:50%;background:#2a6f8a;display:block}
.dots i.on{background:#fff}

/* footer */
.fbox{background:#fff;border-radius:5px;text-align:center;padding-top:16px;box-shadow:0 4px 10px rgba(0,0,0,.2)}
.fbox h4{font-family:"Fira Sans",sans-serif;font-weight:600;font-size:15px;color:#7a1040;margin-bottom:9px}
.fbox li{list-style:none;font-size:13.5px;line-height:27px;color:var(--teal)}
.fbox li.strong{font-family:"Fira Sans",sans-serif;font-weight:600;color:var(--teal)}
.emblem{left:686px;top:1917px;width:107px;height:140px;border-radius:50% 50% 40% 40%;background:rgba(255,255,255,.12)}
.contact{left:847px;top:1911px;width:240px;text-align:center;font-family:"Fira Sans",sans-serif;font-weight:500;font-size:14px;line-height:20.5px;color:#fff}
.contact .gap{height:16px}
</style>
</head>
<body>
<div class="page">
  <div class="abs topline"></div>
  <header class="abs header"></header>
  <div class="abs brand">Calloway Headache Clinics <i></i></div>
  <nav class="abs nav">
    <span class="drop">Calloway Method®</span>
    <span class="drop">About</span>
    <span class="drop">Research</span>
    <span class="drop">Patient Reviews</span>
    <span class="drop">FAQ</span>
    <span>Ask Our Patients</span>
    <span>Free Webinar</span>
    <span>Contact Us</span>
  </nav>
  <div class="abs consult">FREE CONSULT</div>

  <div class="abs hero" role="img" aria-label="Photograph of the Dallas city skyline behind a highway overpass"></div>
  <h1 class="abs hero-title">Webinar Registration</h1>
  <svg class="abs hero-curve" width="1200" height="210" viewBox="0 430 1200 210">
    <path d="M0 640 Q600 440 1200 640 L1200 640 L0 640 Z" fill="#fff"/>
    <path d="M0 640 Q600 440 1200 640" fill="none" stroke="var(--green)" stroke-width="5"/>
    <path d="M0 640 Q600 446 1200 640 L1200 645 L0 645 Z" fill="#fff"/>
  </svg>

  <h2 class="abs intro">The Calloway Method® Free Webinar Registration</h2>
  <div class="abs topics-title">Webinar Topics</div>

  <div class="abs topic" style="top:827px">
    <div class="ico"><svg width="16" height="14"><rect x="1" y="6" width="3.5" height="8" fill="#fff"/><rect x="6.3" y="1" width="3.5" height="13" fill="#fff"/><rect x="11.6" y="4" width="3.5" height="10" fill="#fff"/></svg></div>
    <h3>The Numbers</h3><span class="caret">▲</span>
    <p>The procedure’s compelling statistics: performed for over 25 years, more than 1000 patients, and a greater than 80% success rate!</p>
  </div>
  <div class="abs topic" style="top:957px">
    <div class="ico"><svg width="18" height="18"><circle cx="9" cy="9" r="7" fill="none" stroke="#fff" stroke-width="1.6"/><path d="M5.5 9.2 L8 11.5 L12.5 6.5" fill="none" stroke="#fff" stroke-width="1.8"/></svg></div>
    <h3>The Benefits</h3><span class="caret">▼</span>
  </div>
  <div class="abs topic" style="top:1021px">
    <div class="ico"><span style="color:#fff;font-family:'Fira Sans',sans-serif;font-weight:700;font-size:20px">?</span></div>
    <h3>The Answers To Faqs</h3><span class="caret">▼</span>
  </div>
  <div class="abs topic" style="top:1085px">
    <div class="ico"><svg width="16" height="14"><rect x="1" y="1" width="14" height="12" rx="2" fill="none" stroke="#fff" stroke-width="1.8"/><circle cx="6" cy="6" r="2" fill="#fff"/></svg></div>
    <h3>The Media</h3><span class="caret">▼</span>
  </div>
  <div class="abs topic" style="top:1149px">
    <div class="ico"><svg width="18" height="18"><circle cx="9" cy="9" r="6.5" fill="none" stroke="#fff" stroke-width="1.6" stroke-dasharray="8 3"/><circle cx="9" cy="9" r="2.4" fill="#fff"/></svg></div>
    <h3>The Treatment Process</h3><span class="caret">▼</span>
  </div>
  <div class="abs topic" style="top:1213px">
    <div class="ico"><svg width="16" height="16"><rect x="1" y="7" width="3.5" height="8" fill="#fff"/><path d="M6 7 L9 1.5 Q11 1.5 10.5 5 L14.5 5 Q15.5 6 14.5 14.5 L6 14.5 Z" fill="#fff"/></svg></div>
    <h3>The Patient Stories</h3><span class="caret">▼</span>
  </div>

  <form class="abs card">
    <h2>Webinar Registration Form</h2>
    <span class="lbl" style="left:29px;top:96px">First Name *</span>
    <span class="lbl" style="left:300px;top:96px">Last Name *</span>
    <div class="fld" style="left:29px;top:129px">Jane</div>
    <div class="fld" style="left:300px;top:129px">Carter</div>

    <span class="lbl" style="left:29px;top:207px">Email Address *</span>
    <span class="lbl" style="left:300px;top:207px">Contact Number *</span>
    <div class="fld" style="left:29px;top:240px">janecarter@example.com</div>
    <div class="fld" style="left:300px;top:240px">+1 555 0100 0000</div>

    <span class="lbl" style="left:29px;top:317px">Diagnosis *</span>
    <span class="lbl" style="left:300px;top:317px">Insurance Carrier *</span>
    <div class="fld" style="left:29px;top:350px">Select <span class="tri">▼</span></div>
    <div class="fld" style="left:300px;top:350px">Select <span class="tri">▼</span></div>
    <div class="hint" style="left:29px;top:416px">Please select the one that best applies to you.</div>
    <div class="hint" style="left:300px;top:416px"><b>Note:</b> We do not accept Keystone Health, Medicaid, or Workers' Compensation.</div>

    <span class="lbl" style="left:29px;top:476px">Message</span>
    <div class="msg">Your Message Goes Here.......</div>

    <span class="lbl" style="left:29px;top:642px">Acknowledgment *</span>
    <div class="agree"><i></i>I agree with the site's User Agreement and Privacy Policy.</div>
    <p class="policy">Please read the site's <a>Terms of Use</a> and <a>Privacy Policy</a> Checking the box acknowledges that you have read, understand, and agree to the site's policies.</p>
    <div class="submit">View Webinar Now</div>
  </form>

  <div class="abs footer-bg"></div>
  <svg class="abs testimonial" width="1200" height="430" viewBox="0 1397 1200 430">
    <path d="M0 1397 H1200 V1714 Q600 1930 0 1714 Z" fill="var(--night)"/>
  </svg>
  <div class="abs quote-mark">”</div>
  <p class="abs quote">Can hardly wait. Had my trial last month, permanent 8/31. Works amazing. I have had migraines for over 50 years and tried so many things.</p>
  <div class="abs author">Marlene</div>
  <div class="abs dots"><i></i><i class="on"></i><i></i></div>

  <div class="abs fbox" style="left:138px;top:1915px;width:192px;height:163px">
    <h4>WE OFFER</h4>
    <ul><li class="strong">FREE WEBINAR</li><li>Migraine Treatment</li><li>Calloway Method</li><li>Headache Help</li></ul>
  </div>
  <div class="abs fbox" style="left:381px;top:1915px;width:193px;height:185px">
    <h4>AT A GLANCE</h4>
    <ul><li>Locations</li><li>Terms of Use</li><li>Privacy Policy</li><li>Sitemap</li><li>Contact</li></ul>
  </div>
  <div class="abs emblem" role="img" aria-label="Line illustration of a head in profile"></div>
  <address class="abs contact" style="font-style:normal">
    Calloway Headache Clinics<div class="gap" style="height:5px"></div>
    Corporate Headquarters<br>4820 Larkspur Parkway<br>Suite 210<br>Dallas, Texas 75219
    <div class="gap"></div>
    Main: (800) 555-0142<br>or (214) 555-0187<br>After Hours: (972) 555-0163<br>Fax: (855) 555-0119
  </address>
</div>
</body>
</html>
```